Info-Flyer für Sandstrahlen in fotorealistischer Darstellung
Zielgruppe
Wir sind ein etablierter Steinmetzbetrieb und fertigen hauptsächlich individuelle Grabmale.
Zusätzlich möchten wir in Zunkunft folgende Leistungen anbieten:
- Sandstrahlen in fotorealistischer Darstellung (Details bis zur Stärke eines menschlichen Haares 1/20 mm- von jeder Vorlage wie Skizze, Foto, Zeichnung oder Gemälde; feinste Schriften und Sprüche):
auf polierten, rauen, unebenen und gewölbeten Oberflächen aus Stein, Glas, Porzellan, Fliesen, Metall und anderen Materialien
Die Technik bringt feinere Ergebnisse wie Lasergravur (vorallem im Fotobereich)
Beispiele:
Weinetikett auf Glasflasche, Motive auf Duschglastüren, Logo auf Glastür, Logo auf Kieselstein als Visitenkarte, Gravur auf Urne, Türschild auf Metall, Firmenschild, Foto auf beleuchtetem Glas, Pokale, Wortsteine. Die Texte bitte wie angegeben im Word Dokument. Die Adressdaten bitte von unserer Seite
www.steinmetz-bölting.de unter 'Kontakt' entnehmen. Die Farben sollten sich an den Logofarben schwarz weiß gold orientieren.
Die Bilder der genannten Webseite könne als Platzhalter verwendet werden. Später sollen die Bilder von uns selbst verwendet werden. Es wird im Rahmen des Wettbewerbs also ein Grundgerüst gesucht das zu unserem Logo passt. (Farblich und grafisch).
Unsere Zielgruppen sind:
- Werbeagenturen, Fotoläden, Bestattungsunternehmen, Vereine, Privatpersonen, städtische Einrichtungen, Baumärkte, Handwerker, Geschenkartikelläden, Firmen die Weihnachtspräsente suchen etc.
Aufgabenstellung
Erstellung eines Infoflyers (ein- oder mehrseitig) um unsere neuen Leistungen zu präsentieren und zu bewerben.

```html
<!DOCTYPE html>
<html lang="de">
<head>
<meta charset="utf-8">
<title>Info-Flyer Sandstrahlen – Bölting Grabmalwerk</title>
<link rel="stylesheet" href="https://fonts.googleapis.com/css2?family=Signika:wght@600&family=Great+Vibes&family=Open+Sans:wght@400;600&family=Roboto+Condensed:wght@300;400&display=swap">
<style>
:root{
  --bg:#cfd2d5;
  --dark:#2f3031;
  --gold:#c2b27e;
  --gold-deep:#b5a36b;
  --white:#ffffff;
  --paper:#f1f1f1;
  --ink:#3a3a3a;
  --muted:#7b7b7b;
}
*{margin:0;padding:0;box-sizing:border-box}
html,body{width:1200px;height:660px;overflow:hidden;background:var(--bg)}
.canvas{position:relative;width:1200px;height:660px}
.spread{position:absolute;top:110px;width:560px;height:440px;overflow:hidden;box-shadow:0 10px 30px rgba(0,0,0,.18)}
.spread--inside{left:25px;background:var(--paper)}
.spread--outside{left:615px;background:var(--white)}
.abs{position:absolute}
.photo{position:absolute}

.headline{font-family:"Signika",sans-serif;font-weight:600;color:var(--gold);line-height:1}
.headline .script{display:block;font-family:"Great Vibes",cursive;font-weight:400;font-size:1.6em;margin-left:2.6em;margin-top:-.15em}
.body-copy{font-family:"Open Sans",sans-serif;font-size:7.4px;line-height:1.42;color:#e9e9e9}

/* inside spread */
.intro-panel{left:0;top:0;width:215px;height:275px;background:var(--dark);padding:42px 22px 0 36px}
.intro-panel .headline{font-size:15px;margin-bottom:10px}
.more-info{position:absolute;left:36px;bottom:22px;font-family:"Open Sans",sans-serif;font-size:6.5px;color:#ddd;line-height:1.3}
.more-info span{color:var(--gold)}
.services{left:215px;top:105px;width:345px;height:75px;background:var(--white);padding:14px 0 0 28px}
.services h2{font-family:"Signika",sans-serif;font-weight:600;font-size:14px;color:var(--gold)}
.service-list{display:flex;gap:22px;margin-top:8px;padding-left:30px;list-style:none}
.service-list li{font-family:"Roboto Condensed",sans-serif;font-size:7px;line-height:1.15;color:var(--ink);text-transform:uppercase}
.service-list li b{display:block;font-weight:400;font-size:8px}
.divider{left:215px;top:180px;width:345px;height:1px;background:#cfcfcf}
.placeholder{left:250px;top:205px;font-family:"Roboto Condensed",sans-serif;font-size:10px;line-height:1.35;color:var(--ink);text-transform:uppercase}
.placeholder span{display:block;font-weight:300;color:var(--muted)}
.contact-panel{left:0;top:0;width:560px;height:440px;background:var(--gold-deep);clip-path:polygon(502px 180px,560px 180px,560px 440px,400px 440px)}
.contact{right:24px;top:250px;text-align:right;color:var(--white);font-family:"Signika",sans-serif}
.contact .name{font-size:14px;line-height:1.1}
.contact .role{font-size:8px;margin-top:2px;padding-bottom:8px;border-bottom:1px solid rgba(255,255,255,.7)}
.contact-lines{margin-top:28px;font-family:"Open Sans",sans-serif;font-size:6.6px;line-height:1.5;font-weight:400}
.address{margin-top:14px}

/* outside spread */
.text-panel{left:0;top:0;width:222px;height:330px;background:var(--dark);padding:26px 20px 0 24px}
.text-panel .headline{font-size:14px;margin-bottom:14px}
.text-panel .headline::before{content:"";position:absolute;left:24px;top:59px;width:50px;height:1px;background:var(--gold)}
.rule{height:1px;background:#6a6a6a;margin:9px 0 8px}
.tagline{font-family:"Open Sans",sans-serif;font-size:15px;line-height:1.12;color:var(--white)}
.granite-caption{left:243px;top:298px;font-family:"Roboto Condensed",sans-serif;font-size:14px;color:var(--white)}
.cover-panel{left:402px;top:0;width:158px;height:440px;background:var(--dark)}
.brand-name{left:402px;top:196px;width:158px;text-align:center;font-family:"Open Sans",sans-serif;font-weight:400;font-size:14px;color:var(--gold)}
.cover-url{left:402px;top:410px;width:158px;text-align:center;font-family:"Open Sans",sans-serif;font-size:9px;color:var(--gold)}
</style>
</head>
<body>
<main class="canvas">

  <section class="spread spread--inside" aria-label="Flyer Innenseite">
    <div class="abs intro-panel">
      <h1 class="headline">Gehen Sie neue <span class="script">Wege</span></h1>
      <p class="body-copy">Es wird immer wichtiger, sich von Mitbewerbern abzuheben, den Kunden Neues zu bieten und Gründe zu liefern, zu Ihnen zu kommen und nicht zu Ihrem Mitbewerber. Stellen Sie diese neuen Möglichkeiten in Ihrer Gegend vor - wir unterstützen Sie gerne dabei. Denn wenn Kunden zu Ihnen kommen und nach fotorealistischen sandgestrahlten Motiven fragen, dann war Ihr Mitbewerber mit diesem Angebot schneller am</p>
      <p class="more-info">Für mehr information:<br><span>www.strahlglanz-werk.de</span></p>
    </div>

    <div class="photo" role="img" aria-label="Gravierte Glastafel mit Blumenranken" style="left:215px;top:0;width:130px;height:105px;background:linear-gradient(135deg,#7f7589,#5f566a);clip-path:polygon(40px 0,130px 0,90px 105px,0 105px)"></div>
    <div class="photo" role="img" aria-label="Ornamentgravur auf Glas" style="left:305px;top:0;width:150px;height:105px;background:linear-gradient(135deg,#a9a9a9,#6f6f6f);clip-path:polygon(30px 0,150px 0,110px 105px,0 105px)"></div>
    <div class="photo" role="img" aria-label="Fotogravur eines jungen Hundes" style="left:415px;top:0;width:145px;height:105px;background:linear-gradient(135deg,#f2f2f2,#cfcfcf);clip-path:polygon(40px 0,145px 0,145px 105px,0 105px)"></div>

    <div class="abs services">
      <h2>Alle Arbeiten auf Anfrage</h2>
      <ul class="service-list">
        <li>Naturgetreu<b>Fotowiedergabe</b></li>
        <li>Gravur auf unebenen<b>Natursteinflächen</b></li>
        <li>Zeichnung auf<b>Granit graviert</b></li>
      </ul>
    </div>
    <div class="abs divider"></div>
    <p class="abs placeholder">Hier kann Ihr Text stehen.........<span>Individuell anspruchsvoll ........</span></p>

    <div class="photo" role="img" aria-label="Gravierter Kieselstein zwischen Blumen" style="left:0;top:275px;width:215px;height:165px;background:linear-gradient(135deg,#6a5e7c,#4b4a3c 60%,#8a8378)"></div>
    <div class="photo" role="img" aria-label="Zwei Handwerker mit gravierter Steintafel im Garten" style="left:190px;top:275px;width:260px;height:165px;background:linear-gradient(135deg,#5d6f45,#3d4a31 55%,#8b8c7c);clip-path:polygon(25px 0,260px 0,210px 165px,0 165px)"></div>

    <div class="abs contact-panel"></div>
    <div class="abs contact">
      <p class="name">Lukas<br>Bölting</p>
      <p class="role">Steinmetzmeister</p>
      <div class="contact-lines">
        <p>Tel. +49 (0 12 34) 56 78 90<br>Fax +49 (0 12 34) 56 78 91<br>E-Mail: info@strahlglanz-werk.de</p>
        <p class="address">SteinWerk &amp; StrahlBild e.K.<br>Hans-Dieter Rauch<br>Westliche Talstraße 14<br>73099 Musterbach</p>
      </div>
    </div>
  </section>

  <section class="spread spread--outside" aria-label="Flyer Außenseite">
    <div class="abs text-panel">
      <h1 class="headline">Gehen Sie neue <span class="script">Wege</span></h1>
      <p class="body-copy">Es wird immer wichtiger, sich von Mitbewerbern abzuheben, den Kunden Neues zu bieten und Gründe zu liefern, zu Ihnen zu kommen und nicht zu Ihrem Mitbewerber. Stellen Sie diese neuen Möglichkeiten in Ihrer Gegend vor - wir unterstützen Sie gerne dabei. Denn wenn Kunden zu Ihnen kommen und nach fotorealistischen sandgestrahlten Motiven fragen, dann war Ihr Mitbewerber mit diesem Angebot schneller am Markt als Sie. Nutzen Sie den Vorsprung - heben Sie sich ab und erschließen Sie die Märkte, bevor es andere tun. Zum Kontakt</p>
      <div class="rule"></div>
      <p class="tagline">Individuell.<br>Anspruchsvoll.<br>Wertbeständig.</p>
    </div>

    <div class="photo" role="img" aria-label="Spiralförmige Linienzeichnung auf Granit graviert" style="left:226px;top:0;width:172px;height:330px;background:radial-gradient(circle at 45% 35%,#8e7d66,#5e5042 70%);clip-path:polygon(30px 0,172px 0,172px 330px,0 330px)"></div>
    <p class="abs granite-caption">Auf Granit graviert</p>

    <div class="photo" role="img" aria-label="Dekorative Schwarz-Weiß-Muster in Stein graviert" style="left:0;top:334px;width:292px;height:106px;background:linear-gradient(90deg,#3f3d45,#6a6778 50%,#4a4858)"></div>
    <div class="photo" role="img" aria-label="Galoppierendes Pferd auf dunklem Granit" style="left:270px;top:334px;width:128px;height:106px;background:linear-gradient(135deg,#8a8c90,#3c3e44);clip-path:polygon(24px 0,128px 0,128px 106px,0 106px)"></div>

    <div class="abs cover-panel"></div>
    <p class="abs brand-name">Bölting Grabmalwerk</p>
    <p class="abs cover-url">www.strahlglanz-werk.de</p>
  </section>

</main>
</body>
</html>
```